New Business Card for Innovative Tool Company

We need a new design of business card for our florida based tool manufacturing company. I will attach 2 files that we use for our logo, use whichever you feel works best for the card. Main colours are as per logo, and we can use different shades of black/white/grey for the background.

Contact Information for Business Card

Name/Jobtitle/cell
Brackwell Tools
Suite 214c
3190 Harlowmere Pkw
Orlando, FL32819
USA
name@brackwellco.example
www.brackwellco.example

Font styles to use
Sans Serif

Colors

Designer to choose colors to be used in the design.

Requirements
Must have
• Icons for Chatterly, Quiplet, Snapvista, Findora & Viewtube

```html
<!DOCTYPE html>
<html lang="en">
<head>
<meta charset="utf-8">
<title>Brackwell Tools – Business Card</title>
<link rel="stylesheet" href="https://fonts.googleapis.com/css2?family=Exo+2:wght@700&family=Open+Sans:wght@400;600&display=swap">
<style>
  :root {
    --ink: #0d0d0d;
    --yellow: #f8ec3b;
    --white: #f2f2f2;
    --rule: #3a3a3a;
    --stage: #4a4a4a;
  }
  * { box-sizing: border-box; margin: 0; padding: 0; }
  html, body { width: 1200px; height: 896px; overflow: hidden; }
  body {
    background: var(--stage);
    font-family: "Open Sans", sans-serif;
    display: flex; flex-direction: column; align-items: center; justify-content: center;
    gap: 16px;
  }
  .card { width: 700px; height: 400px; position: relative; overflow: hidden; }

  /* Front */
  .card-front { background: var(--ink); color: var(--white); border-bottom: 10px solid var(--yellow); }
  .holder { position: absolute; left: 56px; top: 92px; }
  .holder-name {
    font-family: "Exo 2", sans-serif; font-weight: 700; color: var(--yellow);
    font-size: 26px; letter-spacing: 1px; text-transform: uppercase; line-height: 1;
    white-space: nowrap;
  }
  .holder-role { font-size: 16px; margin-top: 4px; }
  .contact-list { list-style: none; margin-top: 16px; font-size: 15px; line-height: 1.55; }
  .contact-list li { display: flex; align-items: center; gap: 10px; white-space: nowrap; }
  .contact-list svg { width: 13px; height: 13px; fill: var(--yellow); flex: none; }

  .brand { display: flex; align-items: center; gap: 12px; white-space: nowrap; }
  .brand-mark { width: 46px; height: 46px; border-radius: 50%; border: 3px solid currentColor; flex: none; }
  .brand-name { font-family: "Open Sans", sans-serif; font-weight: 600; font-size: 26px; letter-spacing: 1px; text-transform: uppercase; line-height: 1; }
  .card-front .brand { position: absolute; right: 56px; top: 150px; color: var(--yellow); }

  .front-rule { position: absolute; right: 56px; top: 240px; width: 330px; border-top: 1px solid var(--rule); }
  .address { position: absolute; right: 56px; top: 256px; text-align: right; font-size: 16px; line-height: 1.35; font-style: normal; white-space: nowrap; }
  .address-company { color: var(--yellow); font-size: 17px; text-transform: uppercase; }

  /* Back */
  .card-back { background: var(--yellow); color: var(--ink); }
  .card-back .brand { position: absolute; left: 50%; top: 130px; transform: translateX(-50%); }
  .back-rule { position: absolute; left: 50%; top: 230px; width: 440px; transform: translateX(-50%); border-top: 1.5px solid var(--ink); }
  .social-list {
    position: absolute; left: 0; right: 0; top: 258px;
    list-style: none; display: flex; justify-content: center; gap: 18px;
    font-size: 12px; font-weight: 600;
  }
  .social-list li { display: flex; align-items: center; gap: 5px; white-space: nowrap; }
  .social-list li::before { content: ""; width: 14px; height: 14px; border-radius: 50%; background: var(--ink); }
</style>
</head>
<body>
  <section class="card card-front">
    <div class="holder">
      <h1 class="holder-name">Daniel Corwin</h1>
      <p class="holder-role">Managing Director</p>
      <ul class="contact-list">
        <li><svg viewBox="0 0 12 12"><rect x="3" y="0" width="6" height="12" rx="1"/></svg>555 0142 0199</li>
        <li><svg viewBox="0 0 12 12"><path d="M0 2h12v8H0z M0 2l6 5 6-5"/></svg>name@brackwellco.example</li>
        <li><svg viewBox="0 0 12 12"><circle cx="6" cy="6" r="6"/></svg>www.brackwellco.example</li>
      </ul>
    </div>
    <div class="brand">
      <span class="brand-mark"></span>
      <span class="brand-name">Brackwell Tools</span>
    </div>
    <div class="front-rule"></div>
    <address class="address">
      <div class="address-company">Brackwell Tools</div>
      <div>Suite 214c 3190 Harlowmere Pkw</div>
      <div>Harlow Bay, FL30099 USA</div>
    </address>
  </section>

  <section class="card card-back">
    <div class="brand">
      <span class="brand-mark"></span>
      <span class="brand-name">Brackwell Tools</span>
    </div>
    <div class="back-rule"></div>
    <ul class="social-list">
      <li>Chatterly</li>
      <li>Findora</li>
      <li>Viewtube</li>
      <li>Quiplet</li>
      <li>Snapvista</li>
    </ul>
  </section>
</body>
</html>
```